Business Card Design for a Lending Business (Hard Money loans)

We need a business card for our Real Estate Lending business. We do hard Money loans for real estate investors. We have an existing logo we like, see attached. I'd like the business card to mostly include the logo colors, but a bright color pop of some sort would be nice to see also. Card should include Logo, Company Name, Company Address, Employee Name, Cell Phone, Main Phone, Email, Website

Industry/Entity Type

Finance / Lending

Contact Information for Business Card

Logo, Company Name, Company Address, Employee Name, Cell Phone, Main Phone, Email, Website

Requirements
Nice to have
• I'd like the business card to mostly include the logo colors, but a bright color pop of some sort would be nice to see also.

```html
<!DOCTYPE html>
<html lang="en">
<head>
<meta charset="utf-8">
<title>Harborline Lending – Business Card</title>
<link href="https://fonts.googleapis.com/css2?family=Open+Sans:wght@400;700&display=swap" rel="stylesheet">
<style>
  :root{
    --navy:#283583;
    --cyan:#0aa8dc;
    --ink:#444447;
    --paper:#ffffff;
    --backdrop:#d6d6d6;
  }
  *{margin:0;padding:0;box-sizing:border-box}
  html,body{width:1200px;height:896px;overflow:hidden}
  body{background:var(--backdrop);font-family:"Open Sans",Arial,sans-serif;position:relative}
  .card{position:absolute;left:334px;width:528px;height:300px;border-radius:29px;overflow:hidden}
  .card-front{top:126px;background:var(--paper)}
  .card-back{top:475px;background:var(--navy)}

  .brand{position:absolute;display:flex;flex-direction:column;align-items:center;font-weight:700;text-transform:uppercase;line-height:1}
  .brand-mark{border-radius:50%}
  .card-front .brand{right:24px;top:20px;width:166px;color:var(--navy)}
  .card-front .brand-mark{width:80px;height:80px;border:9px solid var(--navy);margin-bottom:12px}
  .card-front .brand-name{font-size:22px;letter-spacing:2px}
  .card-front .brand-sub{font-size:11px;letter-spacing:5px;margin-top:6px}

  .card-back .brand{left:0;right:0;top:40px;color:var(--paper)}
  .card-back .brand-mark{width:138px;height:138px;border:16px solid var(--paper);margin-bottom:24px}
  .card-back .brand-name{font-size:40px;letter-spacing:6px}
  .card-back .brand-sub{font-size:17px;letter-spacing:8px;margin-top:10px}

  .person{position:absolute;left:24px;top:133px}
  .person-name{font-size:19px;font-weight:700;color:var(--cyan);letter-spacing:-.2px;line-height:1.2}
  .person-title{font-size:14.5px;color:var(--ink);margin-top:2px}

  .divider{position:absolute;left:24px;right:24px;top:196px;height:1.5px;background:var(--navy)}

  .contacts{position:absolute;left:24px;top:211px;list-style:none}
  .contacts li{display:flex;align-items:center;font-size:15px;color:var(--ink);height:19px}
  .contacts svg{width:12px;height:12px;margin-right:7px;fill:var(--cyan)}

  .address{position:absolute;right:24px;top:208px;text-align:right;font-size:14.5px;line-height:19.5px;color:var(--ink)}

  .footer-bands{position:absolute;left:0;bottom:0;width:528px;height:30px}
  .website{position:absolute;right:24px;bottom:8px;font-size:14.5px;color:var(--paper)}
</style>
</head>
<body>
  <section class="card card-front">
    <div class="brand">
      <span class="brand-mark"></span>
      <span class="brand-name">Harborline</span>
      <span class="brand-sub">Lending</span>
    </div>

    <div class="person">
      <p class="person-name">DANIEL ARNETT</p>
      <p class="person-title">Managing Director</p>
    </div>

    <div class="divider"></div>

    <ul class="contacts">
      <li><svg viewBox="0 0 24 24"><path d="M6.6 10.8a15 15 0 0 0 6.6 6.6l2.2-2.2c.3-.3.7-.4 1-.2 1.1.4 2.3.6 3.6.6.6 0 1 .4 1 1V20c0 .6-.4 1-1 1A17 17 0 0 1 3 4c0-.6.4-1 1-1h3.5c.6 0 1 .4 1 1 0 1.3.2 2.5.6 3.6.1.3 0 .7-.2 1z"/></svg>4105550182</li>
      <li><svg viewBox="0 0 24 24"><path d="M7 1h10a2 2 0 0 1 2 2v18a2 2 0 0 1-2 2H7a2 2 0 0 1-2-2V3a2 2 0 0 1 2-2zm0 3v14h10V4zm5 15.5a1 1 0 1 0 0 2 1 1 0 0 0 0-2z"/></svg>41055501470</li>
      <li><svg viewBox="0 0 24 24"><path d="M2 5h20v2l-10 6L2 7zm0 4.3l10 6 10-6V19H2z"/></svg>info@harborln.com</li>
    </ul>

    <p class="address">402 Quarry Ridge Road<br>Easton, MD 21601</p>

    <svg class="footer-bands" viewBox="0 0 528 30" preserveAspectRatio="none" aria-hidden="true">
      <path d="M0 7 H318 L310 12 H0 Z" fill="var(--navy)"/>
      <path d="M0 16 H296 C312 16 320 7 340 2 H528 V30 H0 Z" fill="var(--cyan)"/>
    </svg>
    <p class="website">www.harborline.com</p>
  </section>

  <section class="card card-back">
    <div class="brand">
      <span class="brand-mark"></span>
      <span class="brand-name">Harborline</span>
      <span class="brand-sub">Lending</span>
    </div>
  </section>
</body>
</html>
```